Newly created Management Consulting company needs a brochure to capture clients's interest

This is a new management consulting firm providing service in Finance, Marketing, Operations/Manufacturing Strategy, and Project Management.
Please go to the company's website: www.veltanorpartners.ca . The website is pretty straightforward and gives a clear explanation of all the services and sub-services offered. Based on the existent material on the website, I would like to create a company's brochure that can inspire clients to seek our services.
One important thing: the slogan/tagline ("Shaping the future of your business") needs to be added somewhere in the vicinity of our company's' LOGO. Please see attached the company's logo (JPEG file).
The brochure size and number of pages can vary, depending on the layout of the brochure so it can fit the content, so I am open to different and innovative sizes/shapes and no. of pages etc. Graphics should combine real pictures with graphic design technology, and should give a professional look and feel comparable to big companies' marketing materials.
Updates
The brochure does not necessarily have to include pictures that are on the website. If you think that other pictures and graphics can deliver a stronger message to customers, by all means I am open to any other ideas.
Thanks.
As I said before, the pictures do not need to be exactly the same pictures as on the website, if you can bring in other cool pictures to attract clients, please go ahead. Also, you do not need to use only black background, if you have better colors ideas to combine with the our LOGO, and it looks good, by all means do use other colors. But our LOGO needs to be represented as it is on the JPEG I attached.
May the most creative and cool design win! Good luck!
Please ensure that all the content of our website fits into your brochure, including our contact information. It is up to you to come up with the necessary number of pages, design and shape of the brochure, but the text should be clear enough to be read by a normal person without a magnifying glass.
Thank you.
In order to keep the brochure to a reasonable number of pages, I agree that it is not necessary to include 100% all the text that appears on the website. That being said, even if you do not have enough space to include all the background and introduction paragraphs under each service/sub-service, it is still important that the main message for each service/sub-service is being contained in the brochure.
Target Market(s)
Our clients are companies with sizes starting from 10-20 employees and up to large Larkspan 700 companies.
Industry/Entity Type
Management Consulting
Look and feel

```html
<!DOCTYPE html>
<html lang="en">
<head>
<meta charset="utf-8">
<title>Veltanor Partners – Finance Brochure Spread</title>
<link href="https://fonts.googleapis.com/css2?family=Source+Sans+3:wght@200;300;400;600;700&display=swap" rel="stylesheet">
<style>
  :root{
    --canvas:#d9dadc;
    --green:#7ab648;
    --green-dark:#4f8a2a;
    --green-light:#b5d96a;
    --lime-text:#8cc63f;
    --ink:#2b2b2b;
    --grey-body:#3a3a3a;
    --page-edge:#c9cbcd;
    --strip:#1f2022;
    --strip-text:#8d8f92;
    --photo-a:#e7edf3;
    --photo-b:#9fb2c6;
    --photo-c:#3c4d61;
  }
  *{box-sizing:border-box;margin:0;padding:0}
  html,body{width:1200px;height:793px;overflow:hidden;background:var(--canvas)}
  body{font-family:"Source Sans 3",Arial,sans-serif;color:var(--ink)}

  .spread{position:absolute;left:30px;top:107px;width:1140px;height:579px;display:flex;box-shadow:0 6px 18px rgba(0,0,0,.25)}
  .page{position:relative;width:570px;height:579px;overflow:hidden}

  /* left page */
  .page--services{background:linear-gradient(90deg,#f4f4f4,#e6e7e8)}
  .page__band{position:absolute;left:0;top:0;width:100%;height:20px;background:linear-gradient(180deg,var(--green-light),var(--green))}
  .columns{position:absolute;left:20px;top:44px;right:18px;bottom:34px;display:flex;gap:6px}
  .service{flex:1;background:#fff;border:1px solid var(--page-edge);overflow:hidden;display:flex;flex-direction:column}
  .service__tab{position:relative;background:linear-gradient(180deg,#8cc63f,var(--green-dark));color:#fff;font-weight:700;font-size:12.5px;line-height:1.2;padding:6px 12px 7px;height:50px}
  .service__tab::after{content:"";position:absolute;left:0;bottom:-10px;border-top:10px solid #3d4a2c;border-right:14px solid transparent}
  .service__body{padding:12px 10px 0;font-size:7.4px;line-height:1.28;color:var(--grey-body);overflow:hidden}
  .service__body p{margin-bottom:7px}
  .lead{color:var(--lime-text);font-weight:300;font-size:19px;line-height:.95;text-indent:28px;display:inline}
  .lead--dark{color:var(--green-dark)}
  .page__footer{position:absolute;left:0;bottom:0;width:100%;height:24px;background:var(--strip);color:var(--strip-text);font-size:10px;padding:5px 38px}

  /* right page */
  .page--finance{background:linear-gradient(180deg,#ffffff,#cfd1d3)}
  .finance__band{position:absolute;left:0;top:0;width:100%;height:117px;background:linear-gradient(180deg,var(--green-light) 0%,var(--green) 30%,var(--green-dark) 100%)}
  .finance__title{position:absolute;left:70px;top:12px;font-weight:200;font-size:102px;letter-spacing:6px;color:#fff;line-height:1}
  .finance__photo{position:absolute;left:0;top:117px;width:100%;height:310px;background:linear-gradient(135deg,var(--photo-a) 0%,var(--photo-b) 45%,var(--photo-c) 100%)}
  .finance__intro{position:absolute;left:36px;right:20px;top:440px;font-size:10.6px;line-height:1.42;color:var(--grey-body)}
  .page--finance .page__footer{display:flex;justify-content:flex-end;align-items:center;gap:6px;padding:0 28px}
  .brand{color:var(--green);font-weight:600;font-size:11px}
  .brand__mark{width:9px;height:9px;background:var(--green)}
  .gutter{position:absolute;left:569px;top:0;width:2px;height:100%;background:linear-gradient(90deg,rgba(0,0,0,.15),rgba(0,0,0,0))}
</style>
</head>
<body>
<main class="spread">
  <section class="page page--services">
    <div class="page__band"></div>
    <div class="columns">
      <article class="service">
        <h2 class="service__tab">Capital Budgeting Services</h2>
        <div class="service__body">
          <p><span class="lead">Capital budgeting is the process of analyzing</span> different investment opportunities and deciding which ones to implement. For example, a company has to determine whether to build a new plant or to sink money in an existing facility. Which long-term venture is worth pursuing and will have the greater payoff? Managers need to measure each opportunity's potential in order to compare the projected result, and then make their decision on that information.</p>
          <p>As you can see, a capital budgeting decision defines the future direction and growth of the company. When a company decides on an investment project, the results of that investment decision will affect the business for many years, so care must be taken. Poor capital budgeting can have serious financial consequences. Another example is if a company invests too much in new equipment, it will incur unnecessary high depreciation and other expenses. On the flip-side, if a company does not invest enough, its equipment may not be modern enough to enable it to produce competitively.</p>
          <p>Our consultants help our clients determine capital budgeting decisions by focusing on net present value (NPV) analysis. This determines the effect of each capital budgeting proposal on the company's cash flow, and the consequences of the decision on the company's value. In addition, our consultants will conduct a sensitivity analysis. This helps the client understand which aspects of a project under consideration are the most critical.</p>
        </div>
      </article>
      <article class="service">
        <h2 class="service__tab">Value-Based Management</h2>
        <div class="service__body">
          <p><span class="lead">Increasing the company value</span> is the primary goal for managers. However, meeting quarterly goals is not the same as creating sustainable, long-term value for the shareholders. Managers should balance short-term financial performance against maintaining sustained strong growth and creating value for decades ahead. In fact, pursuing the creation of long-term, sustainable shareholder value is good for all the stakeholders. It creates more jobs, allows companies to show greater commitment in meeting their social responsibilities, and builds the company's reputation and relationships in new markets. This enables the company to be a trusted investment, employer, trade partner, and tax payer.</p>
          <p>Focusing on long-term value creation is a tough job but by relying on data, thoughtful analysis, and a deep understanding of the competitive dynamics in the industry, it can be accomplished. Managers should make decisions on the key driver of value and align their company's overall aspirations, analytical techniques, and management processes to focus on it.</p>
          <p>Veltanor Partners partners with clients to help develop and implement Value Based Management (VBM) strategy and philosophy. This concentrates their businesses on striving to achieve what's important. We help clients fully understand the economic value of their company, identify areas for performance improvement, and implement the most effective strategies for increasing shareholder value.</p>
        </div>
      </article>
      <article class="service">
        <h2 class="service__tab">Business Valuation Services</h2>
        <div class="service__body">
          <p><span class="lead lead--dark">Knowing what their company is worth</span> is a key element in any number of major decisions management may have to consider. Valuing a business requires a deep understanding and analysis of an industry and the firm's position in it. A firm's strategy, products or services, consumer demand, and competitiveness in the industry are just some of the elements determining a company's worth. These are only a few of the characteristics explored when Veltanor Partners values your business. Valuing all or part of a business requires forecasting the future of the business, which in turn requires a disciplined analysis of speculative information and of the financial statements. Good thinking, good application and a good balance between costs and benefits constitute the main ingredients of business valuation.</p>
          <p>Our consultants use their knowledge and expertise to build the best valuation product for our clients and help them understand any gaps between market value and intrinsic value. We provide recommendations that create value for our clients in the event of:</p>
          <p>Merger and Acquisition – we help clients understand the value and synergy to be created through the transaction.<br>Divestitures – we show clients how inefficiencies and negative synergies are eliminated, how the strategic fit and focus are enhanced, and how these affect the market valuation of their firm.</p>
        </div>
      </article>
    </div>
    <footer class="page__footer">www.veltanorpartners.ca</footer>
  </section>

  <section class="page page--finance">
    <div class="finance__band"></div>
    <div class="finance__photo" role="img" aria-label="Photo of business people's hands reviewing financial charts with a tablet and pen"></div>
    <h1 class="finance__title">FINANCE</h1>
    <p class="finance__intro">Making optimal corporate financial decisions to support the execution of corporate strategies has become increasingly challenging in today's competitive and volatile markets. Good, optimal decisions are made based on a thorough understanding of financial information, value-creation as well as all aspects of a particular business. Veltanor Partners can support and advice clients in a variety of industries with their strategic and corporate finance issues in order to maximize shareholder value. Our consultants take a holistic view at the corporate finance and use data-driven cases to help companies understand their sources of valuation advantage and increase returns to shareholders.</p>
    <footer class="page__footer"><span class="brand__mark"></span><span class="brand">Veltanor Partners</span></footer>
  </section>
  <div class="gutter"></div>
</main>
</body>
</html>
```